Büro Vermietung
Velbrin Design Studio hat eine super Arbeit abgeliefert. Wir sind sehr zufrieden mit der Arbeit und natürlich mit dem Design.
Zielgruppe
Bitte keine weiteren Vorschläge mehr. - Wir haben uns bereits für ein Projekte entschieden.
Aufgabenstellung
Interessenten, welche sich für die Büros oder Gewerbefläche interessieren, sollten auf der Webpage folgende Informationen vorfinden:
Menü-Leiste:
HOME / FLÄCHEN / BILDER / LAGE / KONTAKT
HOME:
Titelbild mit dem Hund & weitblick-raeume.ch + Frontbild Liegenschaft
(Zusatztext folgt noch)
FLAECHEN:
Grundriss & Preise
BILDER:
diverse Bilder (folgen noch)
LAGE:
KONTAKT:
(Unsere Adresse) Vermieter /Kontakt
KARELU IMMOBILEN AG

```html
<!DOCTYPE html>
<html lang="de">
<head>
<meta charset="utf-8">
<title>weitblick-raeume.ch – Flächen</title>
<link rel="stylesheet" href="https://fonts.googleapis.com/css2?family=Schoolbell&family=Noto+Sans:wght@400;700&display=swap">
<style>
  :root {
    --brand-red: #cf0a2c;
    --brand-red-dark: #a8061f;
    --ink-purple: #4a4580;
    --text: #444;
    --label: #333;
    --section-grey: #f2f2f2;
    --white: #fff;
  }
  * { margin: 0; padding: 0; box-sizing: border-box; }
  html, body { width: 1200px; height: 1120px; overflow: hidden; background: var(--white); }
  body { position: relative; font-family: "Noto Sans", Verdana, sans-serif; color: var(--text); }

  .header { position: absolute; left: 0; top: 0; width: 1200px; height: 114px; background: var(--white); }
  .brand { position: absolute; left: 291px; top: 64px; z-index: 5; font-family: "Schoolbell", "Comic Sans MS", cursive; font-size: 31px; color: var(--ink-purple); line-height: 1; white-space: nowrap; }

  .mainnav { position: absolute; left: 0; top: 114px; width: 1200px; height: 38px; background: var(--brand-red); }
  .mainnav a { position: absolute; top: 0; height: 38px; line-height: 38px; color: var(--white); text-decoration: none; font-size: 15.5px; letter-spacing: .2px; text-align: center; }
  .mainnav a.active { background: var(--brand-red-dark); font-weight: 700; }

  .mascot { position: absolute; left: 117px; top: 6px; width: 277px; height: 168px; z-index: 3; }
  .mascot .figure { position: absolute; left: 62px; top: 0; width: 104px; height: 162px; border-radius: 44px 44px 12px 12px; background: linear-gradient(180deg, #c9a27a, #efe9e0 55%, #f3f0ea); }
  .mascot .props { position: absolute; left: 0; top: 132px; width: 277px; height: 36px; border-radius: 8px; background: linear-gradient(90deg, #3e5f86 0%, #3e5f86 30%, #f3efe6 40%, #f3efe6 65%, #f2dc6e 75%, #f2dc6e 100%); }

  .hero { position: absolute; left: 0; top: 152px; width: 1200px; height: 200px; background: linear-gradient(90deg, #e4e6e8 0%, #f0f1ef 30%, #dfe2d8 55%, #eaecec 80%, #f3f3f3 100%); border-bottom: 2px solid var(--white); }
  .hero-fade { position: absolute; left: 0; top: 352px; width: 1200px; height: 24px; background: linear-gradient(180deg, #e8ebdf, var(--white)); }

  h2 { font-family: "Schoolbell", "Comic Sans MS", cursive; font-weight: 400; color: var(--ink-purple); font-size: 38px; line-height: 1; }
  p.copy { font-size: 11.7px; line-height: 17px; letter-spacing: .35px; color: var(--text); }

  .property h2 { position: absolute; left: 149px; top: 392px; }
  .property p { position: absolute; left: 149px; top: 442px; width: 575px; }
  .property-photo { position: absolute; left: 740px; top: 404px; width: 295px; height: 213px; background: linear-gradient(180deg, #3c5ea8 0%, #6f8cc7 35%, #d9dde3 55%, #8a8d82 80%, #5f6260 100%); }

  .areas { position: absolute; left: 0; top: 652px; width: 1200px; height: 430px; background: var(--section-grey); }
  .floorplan { position: absolute; left: 155px; top: 34px; width: 225px; height: 203px; background: linear-gradient(135deg, #dbeab0, #f5dd9c); border: 4px solid #777; }
  .pdf-button { position: absolute; left: 149px; top: 262px; width: 263px; height: 35px; background: linear-gradient(180deg, #e0294a, var(--brand-red-dark)); color: var(--white); font-size: 11.5px; line-height: 35px; padding-left: 15px; text-decoration: none; }
  .pdf-button .go { position: absolute; right: 0; top: 0; width: 34px; height: 35px; border-left: 2px solid var(--white); }
  .pdf-button .go svg { position: absolute; left: 10px; top: 11px; }

  .areas h2 { position: absolute; left: 446px; top: 38px; }
  .areas p.copy { position: absolute; left: 446px; top: 90px; width: 570px; }

  .offer { position: absolute; left: 446px; width: 310px; font-size: 10.5px; }
  .offer .row { position: absolute; left: 0; height: 17px; line-height: 17px; white-space: nowrap; }
  .offer .label { position: absolute; left: 0; width: 100px; font-weight: 700; color: var(--label); letter-spacing: .3px; }
  .offer .value { position: absolute; left: 109px; color: var(--label); }
  .offer .total { position: absolute; right: 8px; top: 28px; font-size: 16px; color: var(--ink-purple); }

  .footer { position: absolute; left: 0; top: 1082px; width: 1200px; height: 38px; background: var(--brand-red); color: var(--white); font-size: 11px; line-height: 38px; }
  .footer nav { position: absolute; left: 149px; }
  .footer a { color: var(--white); text-decoration: none; }
  .footer .sep { margin: 0 10px; }
  .footer .copyright { position: absolute; right: 147px; }
</style>
</head>
<body>
  <header class="header">
    <div class="brand">weitblick-raeume.ch</div>
  </header>
  <div class="mascot" role="img" aria-label="Illustration des Maskottchens mit Buch und Notizblock">
    <div class="figure"></div>
    <div class="props"></div>
  </div>

  <nav class="mainnav">
    <a href="#" style="left:570px;width:62px">HOME</a>
    <a href="#" class="active" style="left:639px;width:92px">FLÄCHEN</a>
    <a href="#" style="left:733px;width:76px">BILDER</a>
    <a href="#" style="left:818px;width:62px">LAGE</a>
    <a href="#" style="left:886px;width:90px">KONTAKT</a>
  </nav>

  <div class="hero" role="img" aria-label="Foto eines hellen Grossraumbüros mit grünen Bürostühlen"></div>
  <div class="hero-fade"></div>

  <section class="property">
    <h2>Liegenschaft</h2>
    <p class="copy">Lorem ipsum dolor sit amet, consetetur sadipscing elitr, sed diam nonumy eirmod tempor invidunt ut labore et dolore magna aliquyam erat, sed diam voluptua. At vero eos et accusam et justo duo dolores et ea rebum. Stet clita kasd gubergren, no sea takimata sanctus est Lorem ipsum dolor sit amet. Lorem ipsum dolor sit amet, consetetur sadipscing elitr, sed diam nonumy eirmod tempor invidunt ut labore et dolore magna aliquyam erat, sed diam voluptua. At vero eos et accusam et justo duo dolores et ea rebum. Stet clita kasd gubergren, no sea takimata sanctus est Lorem ipsum dolor sit amet.</p>
    <div class="property-photo" role="img" aria-label="Foto der Liegenschaft: weisses Bürogebäude unter blauem Himmel"></div>
  </section>

  <section class="areas">
    <div class="floorplan" role="img" aria-label="Farbiger Grundriss der Büroetage"></div>
    <a href="#" class="pdf-button">Grundriss als <b>PDF</b> herunterladen
      <span class="go"><svg width="12" height="13" viewBox="0 0 12 13"><path d="M2 1.5 L8 6.5 L2 11.5" fill="none" stroke="#fff" stroke-width="3"/></svg></span>
    </a>

    <h2>Flächen</h2>
    <p class="copy">Lorem ipsum dolor sit amet, consetetur sadipscing elitr, sed diam nonumy eirmod tempor invidunt ut labore et dolore magna aliquyam erat, sed diam voluptua. At vero eos et accusam et justo duo dolores et ea rebum. Stet clita kasd gubergren, no sea takimata sanctus est Lorem ipsum dolor sit amet. Lorem ipsum dolor sit amet, consetetur sadipscing elitr, sed diam nonumy eirmod tempor invidunt ut labore et dolore magn.</p>

    <div class="offer" style="top:188px">
      <div class="row" style="top:0"><span class="label">Fläche:</span><span class="value">1800 m²</span></div>
      <div class="row" style="top:17px"><span class="label">Miete / Monat:</span><span class="value">2000,00&nbsp; CF</span></div>
      <div class="row" style="top:34px"><span class="label">Nebenkosten:</span><span class="value">&nbsp;&nbsp;&nbsp;500,00&nbsp; CF</span></div>
      <div class="total">2500,00 CF</div>
    </div>
    <div class="offer" style="top:262px">
      <div class="row" style="top:0"><span class="label">Fläche:</span><span class="value">900 m²</span></div>
      <div class="row" style="top:17px"><span class="label">Miete / Monat:</span><span class="value">1200,00&nbsp; CF</span></div>
      <div class="row" style="top:34px"><span class="label">Nebenkosten:</span><span class="value">&nbsp;&nbsp;&nbsp;400,00&nbsp; CF</span></div>
      <div class="total">1600,00 CF</div>
    </div>
    <div class="offer" style="top:337px">
      <div class="row" style="top:0"><span class="label">Fläche:</span><span class="value">300 m²</span></div>
      <div class="row" style="top:17px"><span class="label">Miete / Monat:</span><span class="value">500,00&nbsp; CF</span></div>
      <div class="row" style="top:34px"><span class="label">Nebenkosten:</span><span class="value">&nbsp;&nbsp;&nbsp;300,00&nbsp; CF</span></div>
      <div class="total">800,00 CF</div>
    </div>
  </section>

  <footer class="footer">
    <nav><a href="#">Kontakt</a><span class="sep">|</span><a href="#">Impressum</a></nav>
    <span class="copyright">© 2015 weitblick-raeume.ch</span>
  </footer>
</body>
</html>
```